exciting cleaing project

I need a cleaning website built. It has to be built for a woman. the domain name is gwenshines.net.

I need the designer to find the images and code the site. the site needs to be about five pages.

here are some good examples:

https://www.tidypetal.com/gainesville/

http://abrightwren.com/

https://brisknookgainesville.com/services/

https://www.hevo.com/housekeepers/gainesville-fl

https://glintrow.com/

Target Market(s)

home cleaning,

Industry/Entity Type

Cleaning Service

Coding

Coded - Design and coding required

Number of Pages Required

4 page

Font styles to use
Script

Colors
33a6d7
85acd3
f04a50
ec1f27

Requirements
Must have
• nice design
Nice to have
• residential
Should not have
• commercial

```html
<!DOCTYPE html>
<html lang="en">
<head>
<meta charset="utf-8">
<title>Gwen Shines — Residential Cleaning</title>
<link rel="stylesheet" href="https://fonts.googleapis.com/css2?family=Josefin+Sans:wght@400;600;700&family=Open+Sans:wght@400;600;700&display=swap">
<style>
:root{
  --blue:#33a6d7;
  --blue-deep:#2b8ecf;
  --blue-soft:#85acd3;
  --red:#ec1f27;
  --red-soft:#f04a50;
  --ink:#222;
  --text:#555;
  --panel:#f1eced;
  --line:#d8d8d8;
  --white:#fff;
}
*{box-sizing:border-box;margin:0;padding:0}
html,body{width:1200px;height:4680px;overflow:hidden;background:var(--white)}
body{font-family:"Open Sans",sans-serif;color:var(--text);position:relative}
.wave{display:block;margin:10px auto 0}

/* header */
.site-header{position:absolute;left:0;top:0;width:1200px;height:127px;background:var(--white)}
.brand{position:absolute;left:131px;top:22px;display:flex;flex-direction:column;align-items:center;gap:6px}
.brand-dot{width:44px;height:44px;border-radius:50%;background:var(--blue)}
.brand-name{font-family:"Josefin Sans",sans-serif;font-weight:700;font-size:27px;color:var(--blue);letter-spacing:.5px}
.contact-chip{position:absolute;display:flex;align-items:center;gap:12px}
.ring{width:36px;height:36px;border:2px solid var(--blue);border-radius:50%;display:flex;align-items:center;justify-content:center;flex:none}
.chip-label{font-size:12px;color:var(--ink)}
.chip-value{font-family:"Josefin Sans",sans-serif;font-size:17px;color:var(--blue);font-weight:600}
.phone-big{font-family:"Josefin Sans",sans-serif;font-size:23px;color:var(--blue);font-weight:700}
.pill{background:var(--red);color:#fff;font-size:11px;padding:2px 7px;border-radius:3px;letter-spacing:.5px;display:inline-block}
.main-nav{position:absolute;right:131px;top:92px;display:flex;gap:30px;font-size:12.5px;font-weight:600;color:var(--ink)}
.main-nav .on{color:var(--red);border-bottom:2px solid var(--red)}

/* hero */
.hero{position:absolute;left:0;top:127px;width:1200px;height:560px;background:linear-gradient(110deg,#eef0ef 0%,#dfe1e0 45%,#c9b9b1 70%,#a6826f 100%)}
.slide-arrow{position:absolute;top:226px;width:36px;height:44px;background:#333;display:flex;align-items:center;justify-content:center}
.estimate-card{position:absolute;left:131px;top:44px;width:460px;height:456px;background:var(--white);padding:28px 28px}
.estimate-card h1{font-family:"Josefin Sans",sans-serif;font-size:27px;color:var(--ink);font-weight:600;letter-spacing:.5px}
.estimate-card h2{font-size:16px;font-weight:600;color:var(--ink);margin-top:6px;letter-spacing:.5px}
.field-grid{display:grid;grid-template-columns:198px 198px;gap:14px 12px;margin-top:22px}
.field{height:38px;border:1px solid #aaa;font-size:11px;color:#333;padding:11px 14px;letter-spacing:.5px}
.field.wide{grid-column:1/3;height:106px}
.send-btn{margin-top:16px;background:var(--red);color:#fff;font-weight:700;font-size:17px;width:94px;height:40px;display:flex;align-items:center;justify-content:center;font-family:"Josefin Sans",sans-serif}

/* services */
.services{position:absolute;left:0;top:687px;width:1200px;height:837px;background:linear-gradient(180deg,var(--blue-deep),#318fd0);color:#fff;text-align:center}
.section-title{font-family:"Josefin Sans",sans-serif;font-size:30px;font-weight:600;letter-spacing:1px;padding-top:50px}
.svc-grid{position:absolute;left:131px;top:164px;width:940px;display:grid;grid-template-columns:repeat(3,296px);column-gap:26px;row-gap:52px}
.svc-photo{height:166px;position:relative}
.svc-icon{position:absolute;left:50%;bottom:-22px;transform:translateX(-50%);width:48px;height:48px;border-radius:50%;background:#fff;display:flex;align-items:center;justify-content:center}
.svc-name{font-family:"Josefin Sans",sans-serif;font-weight:600;font-size:17px;margin-top:34px}
.svc-text{font-size:13px;line-height:19px;margin:8px auto 0;width:240px;color:#e6f2fb}

/* welcome */
.welcome{position:absolute;left:0;top:1524px;width:1200px;height:516px}
.welcome-photo{position:absolute;left:110px;top:56px;width:240px;height:460px;background:linear-gradient(160deg,#c9b2a2,#5a8fcf 60%,#f2cc2a)}
.welcome-panel{position:absolute;left:323px;top:40px;width:746px;height:476px;background:var(--panel)}
.welcome-copy{position:absolute;left:539px;top:82px;width:470px}
.tag{display:inline-block;background:var(--blue);color:#fff;font-family:"Josefin Sans",sans-serif;font-weight:600;font-size:20px;padding:4px 8px 1px;letter-spacing:.5px}
.welcome-copy h2{font-family:"Josefin Sans",sans-serif;font-size:34px;font-weight:600;color:var(--blue);margin-top:14px;letter-spacing:.5px}
.welcome-copy p{font-size:16px;line-height:27px;color:#333;margin-top:30px}
.call-row{display:flex;gap:16px;align-items:center;margin-top:24px}
.call-row small{font-size:13px;color:#333;display:block}

/* provide */
.provide{position:absolute;left:0;top:2040px;width:1200px;height:751px;background:linear-gradient(180deg,#fff,#eef2f6);text-align:center}
.provide .section-title{color:var(--ink);padding-top:52px}
.offer-card{position:absolute;width:457px;height:262px;background:#fff;box-shadow:0 0 14px rgba(0,0,0,.06);text-align:left;padding:36px 20px 0 134px}
.offer-card svg{position:absolute;left:38px;top:36px}
.offer-card h3{font-family:"Josefin Sans",sans-serif;font-size:17px;font-weight:600;color:var(--blue);line-height:21px;letter-spacing:.5px}
.offer-card h4{font-size:12.5px;font-weight:700;color:var(--ink);margin-top:14px;letter-spacing:.3px}
.offer-card p{font-size:12.5px;line-height:17.5px;color:#444;margin-top:20px}

/* testimonials */
.testimonials{position:absolute;left:0;top:2791px;width:1200px;height:551px;background:linear-gradient(100deg,#8d8478 0%,#d8d2ca 30%,#ece9e5 55%,#cfc6b8 80%,#9c8e7a 100%)}
.quote-frame{position:absolute;left:212px;top:74px;width:776px;height:396px;border:10px solid rgba(133,172,211,.7);background:#fff;text-align:center}
.quote-frame h2{font-family:"Josefin Sans",sans-serif;font-size:30px;font-weight:600;color:var(--ink);margin-top:56px;letter-spacing:.5px}
.quote-frame p{font-size:18px;line-height:28px;color:#444;width:540px;margin:34px auto 0}
.qmark{position:absolute;font-family:"Josefin Sans",sans-serif;font-size:80px;color:#444;font-weight:700;line-height:1}
.quote-frame .rule{width:50px;height:3px;background:var(--blue);margin:40px auto 0}
.quote-frame .who{font-family:"Josefin Sans",sans-serif;font-weight:600;color:var(--blue);font-size:18px;margin-top:16px;letter-spacing:.5px}
.round-arrow{position:absolute;top:267px;width:40px;height:40px;border-radius:50%;background:#fff;display:flex;align-items:center;justify-content:center}

/* blog */
.blog{position:absolute;left:0;top:3342px;width:1200px;height:594px;text-align:center}
.blog .section-title{color:var(--ink);padding-top:60px}
.post{position:absolute;top:158px;width:298px;text-align:left}
.post-photo{height:190px}
.post h3{font-size:15.5px;font-weight:700;color:var(--ink);line-height:21px;margin-top:28px}
.post p{font-size:13px;line-height:18px;color:#444;margin-top:14px}
.more-btn{display:inline-block;background:var(--red);color:#fff;font-size:11px;font-weight:700;padding:7px 8px;border-radius:3px;margin-top:16px}

/* call to action */
.cta{position:absolute;left:0;top:3936px;width:1200px;height:400px;background:linear-gradient(90deg,#3b95d4,#2f87cc 50%,#4b9ad2);color:#fff;text-align:center}
.cta h2{font-family:"Josefin Sans",sans-serif;font-size:29px;font-weight:600;line-height:38px;letter-spacing:1px;padding-top:138px}
.cta-btn{display:inline-block;margin-top:30px;background:#fff;color:var(--blue);font-family:"Josefin Sans",sans-serif;font-weight:700;font-size:20px;padding:20px 28px 16px;letter-spacing:.5px}

/* footer */
.site-footer{position:absolute;left:0;top:4336px;width:1200px;height:282px}
.foot-brand{position:absolute;left:131px;top:48px;display:flex;flex-direction:column;align-items:center;gap:10px}
.foot-call{position:absolute;left:435px;top:62px;display:flex;gap:16px;align-items:flex-start}
.foot-call small{font-size:12.5px;font-weight:600;color:var(--ink);display:block}
.foot-nav{position:absolute;left:131px;top:160px;width:594px;border-top:1px solid var(--line);border-bottom:1px solid var(--line);height:56px;display:flex;align-items:center;justify-content:center;font-size:13px;color:#333;gap:8px}
.hours{position:absolute;left:843px;top:50px;font-size:13px;line-height:26px;color:#333}
.hours h3{font-size:12.5px;font-weight:700;color:var(--ink);border-bottom:2px solid var(--blue);display:inline-block;margin-bottom:8px;line-height:20px}
.bottom-bar{position:absolute;left:0;top:4618px;width:1200px;height:62px;background:#f3f3f3;font-size:12px;color:#333}
.social{position:absolute;left:131px;top:18px;display:flex;gap:8px;align-items:center;font-weight:700}
.social span.dot{width:26px;height:26px;border-radius:50%;display:inline-block}
.copy{position:absolute;left:848px;top:24px}
.ver{position:absolute;left:1142px;top:24px}
</style>
</head>
<body>

<header class="site-header">
  <div class="brand"><span class="brand-dot"></span><span class="brand-name">GWEN SHINES</span></div>
  <div class="contact-chip" style="left:585px;top:24px">
    <span class="ring"><svg width="16" height="12" viewBox="0 0 16 12"><rect x="1" y="1" width="14" height="10" fill="none" stroke="#33a6d7" stroke-width="1.6"/><path d="M1 1l7 6 7-6" fill="none" stroke="#33a6d7" stroke-width="1.6"/></svg></span>
    <div><div class="chip-label">E MAIL US</div><div class="chip-value">info@gwenshines</div></div>
  </div>
  <div class="contact-chip" style="left:830px;top:22px">
    <span class="ring"><svg width="16" height="16" viewBox="0 0 24 24"><path d="M6.6 10.8a15 15 0 006.6 6.6l2.2-2.2a1 1 0 011-.2 11 11 0 003.6.6 1 1 0 011 1V20a1 1 0 01-1 1A17 17 0 013 4a1 1 0 011-1h3.5a1 1 0 011 1c0 1.2.2 2.5.6 3.6a1 1 0 01-.3 1z" fill="#33a6d7"/></svg></span>
    <div><div class="phone-big">555-302-4418</div><span class="pill">REQUEST A FREE ESTIMATE</span></div>
  </div>
  <nav class="main-nav"><span class="on">HOME</span><span>ABOUT US</span><span>SERVICES</span><span>BLOG</span><span>TESTIMONIALS</span><span>CONTACT US</span></nav>
</header>

<section class="hero" role="img" aria-label="Woman in purple gloves wiping a kitchen cabinet">
  <div class="slide-arrow" style="left:0"><svg width="10" height="16"><path d="M8 2L2 8l6 6" stroke="#fff" stroke-width="2" fill="none"/></svg></div>
  <div class="slide-arrow" style="right:0"><svg width="10" height="16"><path d="M2 2l6 6-6 6" stroke="#fff" stroke-width="2" fill="none"/></svg></div>
  <form class="estimate-card">
    <h1>RESIDENTIAL CLEAN</h1>
    <h2>GET A FREE ESTIMATE</h2>
    <div class="field-grid">
      <div class="field">NAME</div><div class="field">EMAIL</div>
      <div class="field">SUBJECT</div><div class="field">PHONE</div>
      <div class="field">ADDRESS</div><div class="field">ADDRESS I</div>
      <div class="field wide">MESSAGE</div>
    </div>
    <div class="send-btn">SEND</div>
  </form>
</section>

<section class="services">
  <h2 class="section-title">OUR SERVICES</h2>
  <svg class="wave" width="56" height="8" viewBox="0 0 56 8"><path d="M0 4q3.5-4 7 0t7 0 7 0 7 0 7 0 7 0 7 0 7 0" stroke="#fff" stroke-width="2" fill="none"/></svg>
  <div class="svc-grid">
    <div><div class="svc-photo" role="img" aria-label="Bedroom interior" style="background:linear-gradient(135deg,#4a4a4e,#cfc8c0)"><span class="svc-icon"><svg width="24" height="20"><rect x="2" y="8" width="20" height="7" fill="#33a6d7"/><rect x="4" y="3" width="16" height="5" fill="#33a6d7"/><rect x="2" y="15" width="2" height="4" fill="#33a6d7"/><rect x="20" y="15" width="2" height="4" fill="#33a6d7"/></svg></span></div><div class="svc-name">Bedroom Interior</div><p class="svc-text">Lorem ipsum dolor sit amet consectetur adipiscing elit sed do eiusmod tempor incididu.</p></div>
    <div><div class="svc-photo" role="img" aria-label="Bright bathroom" style="background:linear-gradient(135deg,#d9dde0,#8d9598)"><span class="svc-icon"><svg width="24" height="20"><path d="M2 10h20v3a5 5 0 01-5 5H7a5 5 0 01-5-5z" fill="#33a6d7"/><rect x="4" y="2" width="3" height="8" fill="#33a6d7"/></svg></span></div><div class="svc-name">Bathrooms</div><p class="svc-text">Lorem ipsum dolor sit amet consectetur adipiscing elit sed do eiusmod tempor incididu.</p></div>
    <div><div class="svc-photo" role="img" aria-label="Modern kitchen" style="background:linear-gradient(135deg,#3d3a38,#d7d4cf)"><span class="svc-icon"><svg width="24" height="20"><path d="M12 2a7 7 0 017 7H5a7 7 0 017-7z" fill="#33a6d7"/><path d="M6 12v6M10 12v6M14 12v6M18 12v6" stroke="#33a6d7" stroke-width="1.6"/></svg></span></div><div class="svc-name">Kitchen</div><p class="svc-text">Lorem ipsum dolor sit amet consectetur adipiscing elit sed do eiusmod tempor incididu.</p></div>
    <div><div class="svc-photo" role="img" aria-label="Dining room" style="background:linear-gradient(135deg,#55595c,#e6e2dc)"><span class="svc-icon"><svg width="24" height="20"><rect x="3" y="5" width="18" height="3" fill="#33a6d7"/><path d="M5 8v10M19 8v10M9 8v10M15 8v10" stroke="#33a6d7" stroke-width="1.8"/></svg></span></div><div class="svc-name">Dining room</div><p class="svc-text">Lorem ipsum dolor sit amet consectetur adipiscing elit sed do eiusmod tempor incididu.</p></div>
    <div><div class="svc-photo" role="img" aria-label="Living room with fireplace" style="background:linear-gradient(135deg,#8f8d89,#e3e1dd)"><span class="svc-icon"><svg width="24" height="20"><rect x="5" y="4" width="14" height="8" rx="2" fill="#33a6d7"/><rect x="2" y="10" width="20" height="6" rx="2" fill="#33a6d7"/></svg></span></div><div class="svc-name">Living room</div><p class="svc-text">Lorem ipsum dolor sit amet consectetur adipiscing elit sed do eiusmod tempor incididu.</p></div>
    <div><div class="svc-photo" role="img" aria-label="Colourful kids room" style="background:linear-gradient(135deg,#f4f2ee,#d8c6b0 60%,#b6d05c)"><span class="svc-icon"><svg width="24" height="20"><circle cx="8" cy="5" r="3" fill="#33a6d7"/><circle cx="16" cy="5" r="3" fill="#33a6d7"/><rect x="4" y="9" width="8" height="10" rx="3" fill="#33a6d7"/><rect x="12" y="9" width="8" height="10" rx="3" fill="#33a6d7"/></svg></span></div><div class="svc-name">Kids rooms</div><p class="svc-text">Lorem ipsum dolor sit amet consectetur adipiscing elit sed do eiusmod tempor incididu.</p></div>
  </div>
</section>

<section class="welcome">
  <div class="welcome-panel"></div>
  <div class="welcome-photo" role="img" aria-label="Smiling cleaner in blue apron and yellow gloves holding a sponge"></div>
  <div class="welcome-copy">
    <span class="tag">WELCOME TO</span>
    <h2>GWEN SHINES</h2>
    <svg width="56" height="8" viewBox="0 0 56 8" style="margin-top:6px"><path d="M0 4q3.5-4 7 0t7 0 7 0 7 0 7 0 7 0 7 0 7 0" stroke="#33a6d7" stroke-width="2" fill="none"/></svg>
    <p>Our mission at Gwen’s Cleaning is simple: to provide high-quality services for our valued clients. Our team goes above and beyond to cater to each project’s specific needs. Through open communication and exceptional service, we hope you’ll find what you’re looking for with our House Cleaning Service. For more information or general inquiries, get in touch today.</p>
    <div class="call-row"><span class="ring"><svg width="16" height="16" viewBox="0 0 24 24"><path d="M6.6 10.8a15 15 0 006.6 6.6l2.2-2.2a1 1 0 011-.2 11 11 0 003.6.6 1 1 0 011 1V20a1 1 0 01-1 1A17 17 0 013 4a1 1 0 011-1h3.5a1 1 0 011 1c0 1.2.2 2.5.6 3.6a1 1 0 01-.3 1z" fill="#33a6d7"/></svg></span><div><small>CALL US NOW ON</small><span class="phone-big">555-302-4418</span></div></div>
  </div>
</section>

<section class="provide">
  <h2 class="section-title">WHAT WE PROVIDE</h2>
  <svg class="wave" width="56" height="8" viewBox="0 0 56 8"><path d="M0 4q3.5-4 7 0t7 0 7 0 7 0 7 0 7 0 7 0 7 0" stroke="#33a6d7" stroke-width="2" fill="none"/></svg>
  <div class="offer-card" style="left:131px;top:160px">
    <svg width="56" height="56" viewBox="0 0 56 56"><rect x="4" y="8" width="48" height="44" rx="4" fill="none" stroke="#ec1f27" stroke-width="3"/><path d="M4 18h48M16 3v10M40 3v10" stroke="#ec1f27" stroke-width="3"/><g fill="#ec1f27"><rect x="14" y="26" width="6" height="5"/><rect x="25" y="26" width="6" height="5"/><rect x="36" y="26" width="6" height="5"/><rect x="14" y="37" width="6" height="5"/><rect x="25" y="37" width="6" height="5"/><rect x="36" y="37" width="6" height="5"/></g></svg>
    <h3>WEEKLY, BI-WEEKLY, MONTHLY<br>OR CUSTOM CLEANS AVAILABLE</h3>
    <h4>ATTENTION TO DETAIL</h4>
    <p>Since its founding, Gwen Shines has been one of the most trusted names in the industry. Hire us for this service and learn how we cater to the needs of each client, ensuring the results you need and deserve.</p>
  </div>
  <div class="offer-card" style="left:609px;top:160px">
    <svg width="50" height="60" viewBox="0 0 50 60"><path d="M14 6h16v8H14zM18 14h10l6 10v30a4 4 0 01-4 4H16a4 4 0 01-4-4V26z" fill="none" stroke="#ec1f27" stroke-width="3"/><path d="M30 8h10" stroke="#ec1f27" stroke-width="3"/><g fill="#ec1f27"><circle cx="44" cy="4" r="2"/><circle cx="47" cy="10" r="2"/><circle cx="42" cy="14" r="2"/></g></svg>
    <h3>MOVE IN &amp; OUT CLEANING</h3>
    <h4 style="margin-top:36px">EXPERT SERVICE</h4>
    <p>We have the experience and skills necessary to tackle just about every type of job that comes our way. With Gwen Shines, clients know exactly what to expect - professionalism, efficiency and exceptional results.</p>
  </div>
  <div class="offer-card" style="left:131px;top:443px">
    <svg width="52" height="56" viewBox="0 0 52 56"><rect x="4" y="4" width="44" height="48" fill="none" stroke="#ec1f27" stroke-width="3"/><path d="M26 4v48M4 28h44M12 16h8M32 16h8M12 40h8" stroke="#ec1f27" stroke-width="3"/></svg>
    <h3>DEEP CLEANING</h3>
    <h4>ALWAYS PREPARED</h4>
    <p>Gwen Shines is committed to getting the job done, especially when it comes to this service. You can count on us to be professional, timely, efficient and make sure you’re satisfied every step of the way.</p>
  </div>
  <div class="offer-card" style="left:609px;top:443px">
    <svg width="60" height="40" viewBox="0 0 60 40"><rect x="4" y="4" width="52" height="24" rx="3" fill="none" stroke="#ec1f27" stroke-width="3"/><rect x="12" y="10" width="14" height="8" fill="none" stroke="#ec1f27" stroke-width="3"/><rect x="34" y="10" width="14" height="8" fill="none" stroke="#ec1f27" stroke-width="3"/><path d="M4 28v10M56 28v10M4 32h52" stroke="#ec1f27" stroke-width="3"/></svg>
    <h3>MODERN BEDROOM</h3>
    <h4 style="margin-top:26px">INTRODUCING GWEN SHINES</h4>
    <h4 style="margin-top:16px">EXCEPTIONAL SERVICE</h4>
  </div>
</section>

<section class="testimonials" role="img" aria-label="Bright living room with plants and dining chairs">
  <div class="round-arrow" style="left:118px"><svg width="10" height="14"><path d="M8 2L3 7l5 5" stroke="#333" stroke-width="2" fill="none"/></svg></div>
  <div class="round-arrow" style="left:1040px"><svg width="10" height="14"><path d="M2 2l5 5-5 5" stroke="#333" stroke-width="2" fill="none"/></svg></div>
  <div class="quote-frame">
    <h2>CUSTOMER TESTIMONIALS</h2>
    <span class="qmark" style="left:66px;top:120px">“</span>
    <p>Sed ut perspiciatis unde omnis iste natus error sit voluptatem accusantium doloremque laudantium, totam rem aperiam, eaque ipsa quae ab illo inventore veritatis et quasi architecto beatae vitae dicta sunt explicabo.</p>
    <span class="qmark" style="left:520px;top:222px">”</span>
    <div class="rule"></div>
    <div class="who">LENA ORTIZ</div>
  </div>
</section>

<section class="blog">
  <h2 class="section-title">LATEST BLOG</h2>
  <svg class="wave" width="56" height="8" viewBox="0 0 56 8"><path d="M0 4q3.5-4 7 0t7 0 7 0 7 0 7 0 7 0 7 0 7 0" stroke="#33a6d7" stroke-width="2" fill="none"/></svg>
  <article class="post" style="left:131px"><div class="post-photo" role="img" aria-label="Gloved hands wiping a surface" style="background:linear-gradient(135deg,#3c3c3c,#e9e6df 50%,#e9c72e)"></div><h3>SED UT PERSPICIATIS UNDE OMNIS ISTE NATUS.</h3><p>Sed ut perspiciatis unde omnis iste natus error sit voluptatem accus antium doloremque.</p><span class="more-btn">READ MORE</span></article>
  <article class="post" style="left:451px"><div class="post-photo" role="img" aria-label="Tidy open-plan living room" style="background:linear-gradient(135deg,#c9c3b9,#f0eeeb 55%,#8a8884)"></div><h3>BUT I MUST EXPLAIN TO YOU HOW ALL THIS MISTAKEN</h3><p>Sed ut perspiciatis unde omnis iste natus error sit voluptatem accus antium doloremque.</p><span class="more-btn">READ MORE</span></article>
  <article class="post" style="left:771px"><div class="post-photo" role="img" aria-label="Cleaner vacuuming a living room floor" style="background:linear-gradient(135deg,#ecebe8,#b8b6b1 50%,#2d8f8a)"></div><h3>AT VERO EOS ET ACCUSAMUS ET IUSTO ODIO DIGNISSIMO</h3><p>Sed ut perspiciatis unde omnis iste natus error sit voluptatem accus antium doloremque.</p><span class="more-btn">READ MORE</span></article>
</section>

<section class="cta" role="img" aria-label="Blue-tinted photo of a cleaner wiping glass">
  <h2>AT VERO EOS ET ACCUSAMUS ET IUSTO<br>ODIO DIGNISSIMOS DUCIMUS QUI BLANDITIIS</h2>
  <span class="cta-btn">SCHEDULE AN APPOINTMENT</span>
</section>

<footer class="site-footer">
  <div class="foot-brand"><span class="brand-dot"></span><span class="brand-name">GWEN SHINES</span></div>
  <div class="foot-call"><span class="ring" style="margin-top:8px"><svg width="16" height="16" viewBox="0 0 24 24"><path d="M6.6 10.8a15 15 0 006.6 6.6l2.2-2.2a1 1 0 011-.2 11 11 0 003.6.6 1 1 0 011 1V20a1 1 0 01-1 1A17 17 0 013 4a1 1 0 011-1h3.5a1 1 0 011 1c0 1.2.2 2.5.6 3.6a1 1 0 01-.3 1z" fill="#33a6d7"/></svg></span><div><small>CALL US NOW ON</small><div class="phone-big">555-302-4418</div><span class="pill">REQUEST A FREE ESTIMATE</span></div></div>
  <nav class="foot-nav"><span>HOME</span>|<span>ABOUT US</span>|<span>SERVICES</span>|<span>BLOG</span>|<span>TESTIMONIALS</span>|<span>CONTACT US</span></nav>
  <div class="hours">
    <h3>OPENING HOURS</h3>
    <div>Contact By Text after 9am -10pm</div>
    <div>Available Cleaning Time</div>
    <div>Every day by appointment</div>
    <div>Mon - Fri:</div>
    <div>9am - 5pm</div>
    <div>Saturday- Sunday: Please Contact</div>
  </div>
</footer>

<div class="bottom-bar">
  <div class="social">FOLLOW US <span class="dot" style="background:#3b5fb0;margin-left:10px"></span><span class="dot" style="background:#2ea1e6"></span><span class="dot" style="background:#1e4f8a"></span></div>
  <div class="copy">Copyright © 2019 All Rights Reserved</div>
  <div class="ver">X37</div>
</div>

</body>
</html>
```